Oven Cleaning Business owner needs business card design

Hi there,
Would like for a business card to be designed for myself, the owner of a professional oven cleaning business on the Sunshine Coast.
Would like it to look sleek, and modern-ish. Bit creative is encouraged too.
Include following:
Name/title: Corin de Walbrek, Owner
Phone number: 1300 482 906
Email: info@kitchenlustrely.com.au
Website: www.kitchenlustrely.com.au

```html
<!DOCTYPE html>
<html lang="en">
<head>
<meta charset="UTF-8">
<title>Kitchen Lustrely – Business Card</title>
<link rel="stylesheet" href="https://fonts.googleapis.com/css2?family=Montserrat:wght@800&family=Arimo:wght@400;700&display=swap">
<style>
  :root {
    --backdrop: #2a2a2a;
    --teal: #17c9cc;
    --ink: #111111;
    --paper: #f7f7f7;
    --rule: #c9c9c9;
    --text: #1a1a1a;
  }
  * { margin: 0; padding: 0; box-sizing: border-box; }
  html, body {
    width: 1200px; height: 750px; overflow: hidden;
    background: var(--backdrop);
  }
  .canvas {
    position: relative; width: 1200px; height: 750px;
    display: flex; align-items: center; justify-content: center; gap: 60px;
  }
  .card {
    position: relative; width: 510px; height: 300px;
    border-radius: 18px; overflow: hidden;
  }
  /* Front */
  .card-front {
    background: var(--teal);
    display: flex; align-items: center; justify-content: center;
  }
  .brand-front {
    font-family: "Montserrat", sans-serif; font-weight: 800;
    font-size: 40px; letter-spacing: 2px; color: var(--ink);
    text-transform: uppercase; line-height: 1.05; text-align: center;
  }
  /* Back */
  .card-back { background: var(--paper); }
  .brand-block {
    position: absolute; left: 40px; top: 95px; width: 185px;
    display: flex; flex-direction: column; align-items: center; gap: 14px;
  }
  .brand-dot {
    width: 62px; height: 62px; border-radius: 50%; background: var(--teal);
  }
  .brand-back {
    font-family: "Montserrat", sans-serif; font-weight: 800;
    font-size: 21px; letter-spacing: 1px; color: var(--ink);
    text-transform: uppercase; line-height: 1.1; text-align: center;
  }
  .divider {
    position: absolute; left: 245px; top: 60px; width: 1px; height: 150px;
    background: var(--rule);
  }
  .contact {
    position: absolute; left: 268px; top: 78px;
    font-family: "Arimo", sans-serif; color: var(--text);
  }
  .contact-name { font-weight: 700; font-size: 19px; }
  .contact-title { color: var(--teal); font-size: 14px; margin-top: 3px; }
  .contact-list { list-style: none; margin-top: 24px; }
  .contact-list li {
    display: flex; align-items: center; gap: 8px;
    font-size: 12.5px; margin-bottom: 6px;
  }
  .contact-list svg { width: 11px; height: 11px; flex: none; fill: var(--teal); }
  .strip-dark {
    position: absolute; left: 0; bottom: 0; width: 345px; height: 12px;
    background: var(--ink);
  }
  .strip-teal {
    position: absolute; right: 0; bottom: 0; width: 165px; height: 12px;
    background: var(--teal);
  }
</style>
</head>
<body>
<main class="canvas">
  <section class="card card-front">
    <h1 class="brand-front">Kitchen<br>Lustrely</h1>
  </section>

  <section class="card card-back">
    <div class="brand-block">
      <span class="brand-dot"></span>
      <span class="brand-back">Kitchen Lustrely</span>
    </div>
    <div class="divider"></div>
    <div class="contact">
      <p class="contact-name">Corin de Walbrek</p>
      <p class="contact-title">Owner</p>
      <ul class="contact-list">
        <li>
          <svg viewBox="0 0 24 24"><path d="M6.6 10.8a15.1 15.1 0 0 0 6.6 6.6l2.2-2.2a1 1 0 0 1 1-.25 11.4 11.4 0 0 0 3.6.57 1 1 0 0 1 1 1V20a1 1 0 0 1-1 1A17 17 0 0 1 3 4a1 1 0 0 1 1-1h3.5a1 1 0 0 1 1 1c0 1.25.2 2.45.57 3.57a1 1 0 0 1-.25 1z"/></svg>
          1300 482 906
        </li>
        <li>
          <svg viewBox="0 0 24 24"><path d="M2 5h20v14H2z" fill="none"/><path d="M2 5h20v2l-10 6L2 7zM2 9l10 6 10-6v10H2z"/></svg>
          info@kitchenlustrely.com.au
        </li>
        <li>
          <svg viewBox="0 0 24 24"><circle cx="12" cy="12" r="10"/></svg>
          www.kitchenlustrely.com.au
        </li>
      </ul>
    </div>
    <div class="strip-dark"></div>
    <div class="strip-teal"></div>
  </section>
</main>
</body>
</html>
```